Tech Savy small Business accountant business card design

We need a business card for a new company based in the cloud. We provide tax, business advisory, accounting, information technology solutions and back office functions to small businesses. We offer fixed fee packages with add on services as you need them. By harnessing technology we simplify small business operational processes providing valuable time and information for small business owners to grow their business. In the logo (quilbrook) we want to be able to see quil and experts. The final design should communicate achieving growth dreams and balance (ie life and $).
Updates
This project has been temporarily placed on hold until I finalize "Tech Savy small Business accountant needs a logo". I invite all designers to submit on this logo project. Once my logo is finalized I will resume this business card contest. Thanks Added Wednesday, March 19, 2014
This project has been temporarily placed on hold until I finalize "Tech Savy small Business accountant logo". I invite all designers to submit on this logo project. Once my logo is finalized I will resume this business card contest. Thanks Added Thursday, March 20, 2014
Target Market(s)
Small Business (Revenue $500,000, more than 3 employees) owners.
Industry/Entity Type
Small Business
Contact Information for Business Card
Marla Henwick (Principal)
Accountant, Tax Agent.
TEL | 0418 663 904
EMAIL | Marla.Henwick@quilbrook-mail.com.au
WEB | www.quilbrook-mail.com.au
Look and feel

```html
<!DOCTYPE html>
<html lang="en">
<head>
<meta charset="utf-8">
<title>Quilbrook business card</title>
<link href="https://fonts.googleapis.com/css2?family=Quicksand:wght@300;400;700&display=swap" rel="stylesheet">
<style>
  :root {
    --bg: #ececec;
    --slate: #737376;
    --sky: #5b96d1;
    --sky-soft: #7aaadb;
    --white: #ffffff;
    --logo-grey: #8e8e91;
  }
  * { margin: 0; padding: 0; box-sizing: border-box; }
  html, body {
    width: 1200px; height: 800px; overflow: hidden;
    background: var(--bg);
    font-family: "Quicksand", sans-serif;
  }
  .canvas { position: relative; width: 1200px; height: 800px; }

  .card {
    position: absolute; top: 241px;
    width: 520px; height: 318px;
    overflow: hidden;
  }

  /* Front: contact side */
  .card--front { left: 50px; background: var(--slate); color: var(--white); }
  .holder-name {
    position: absolute; left: 30px; top: 30px;
    font-size: 38px; font-weight: 700; letter-spacing: -0.5px; white-space: nowrap;
  }
  .holder-role-tag {
    font-size: 13px; font-weight: 400; color: var(--sky-soft); letter-spacing: 0;
    margin-left: 4px;
  }
  .name-rule {
    position: absolute; left: 0; top: 86px; width: 372px; height: 3px; background: var(--white);
  }
  .holder-title {
    position: absolute; right: 148px; top: 94px;
    font-size: 17px; font-weight: 400; white-space: nowrap;
  }
  .contact-list {
    position: absolute; left: 0; right: 30px; top: 138px;
    list-style: none;
  }
  .contact-item {
    display: flex; justify-content: space-between; align-items: baseline;
    height: 32px; padding-left: 160px;
  }
  .contact-label {
    font-size: 15px; font-weight: 300; color: var(--sky-soft); white-space: nowrap;
  }
  .contact-label .divider { color: var(--white); margin-left: 6px; }
  .contact-value { font-size: 17px; font-weight: 400; white-space: nowrap; }
  .brand-band {
    position: absolute; left: 0; right: 0; bottom: 0; height: 62px;
    background: var(--sky);
    display: flex; align-items: center; justify-content: flex-end; padding-right: 26px;
  }
  .brand-band__name {
    font-size: 32px; font-weight: 700; color: var(--slate); letter-spacing: -0.5px;
  }

  /* Back: brand side */
  .card--back { left: 630px; background: var(--white); }
  .brand-mark {
    position: absolute; left: 0; right: 0; top: 92px;
    text-align: center;
  }
  .brand-mark__name {
    display: block;
    font-size: 92px; font-weight: 700; color: var(--logo-grey); letter-spacing: -2px; line-height: 1;
  }
  .brand-mark__tagline {
    display: block; margin-top: 16px;
    font-size: 22px; font-weight: 400; color: var(--logo-grey);
  }
</style>
</head>
<body>
<main class="canvas">
  <section class="card card--front" aria-label="Business card front">
    <h1 class="holder-name">Marla Henwick<span class="holder-role-tag">(Principal)</span></h1>
    <div class="name-rule"></div>
    <p class="holder-title">Accountant, Tax Agent.</p>
    <ul class="contact-list">
      <li class="contact-item"><span class="contact-label">TEL<span class="divider">|</span></span><span class="contact-value">0418 663 904</span></li>
      <li class="contact-item"><span class="contact-label">EMAIL<span class="divider">|</span></span><span class="contact-value">Marla.Henwick@quilbrook-mail.com.au</span></li>
      <li class="contact-item"><span class="contact-label">WEB<span class="divider">|</span></span><span class="contact-value">www.quilbrook-mail.com.au</span></li>
    </ul>
    <div class="brand-band"><span class="brand-band__name">quilbrook</span></div>
  </section>

  <section class="card card--back" aria-label="Business card back">
    <div class="brand-mark">
      <span class="brand-mark__name">quilbrook</span>
      <span class="brand-mark__tagline">Your business and accounting partner</span>
    </div>
  </section>
</main>
</body>
</html>
```